Letterhead

We would like to use the logo attached as a new letterhead. Our problem is that we think the dark blue background is too much. We'd like a sleek, professional letterhead, and we'd like at least five options to choose from. I've also uploaded our old letterhead for reference of the style we're going for.

```html
<!DOCTYPE html>
<html lang="en">
<head>
<meta charset="utf-8">
<title>Harborline Strategies Letterhead</title>
<link href="https://fonts.googleapis.com/css2?family=Crimson+Pro:wght@600&family=Lato:wght@400;700&display=swap" rel="stylesheet">
<style>
  :root {
    --navy: #1c2f4c;
    --gold: #c4a058;
    --gold-band: #d8b466;
    --paper: #ffffff;
    --backdrop: #ececec;
    --text: #2a3446;
  }
  html, body {
    margin: 0;
    width: 970px;
    height: 1200px;
    overflow: hidden;
    background: var(--backdrop);
  }
  .canvas {
    position: relative;
    width: 970px;
    height: 1200px;
  }
  .sheet {
    position: absolute;
    left: 75px;
    top: 20px;
    width: 820px;
    height: 1160px;
    background: var(--paper);
    box-shadow: 0 1px 4px rgba(0,0,0,0.12);
    overflow: hidden;
  }
  .brand {
    position: absolute;
    left: 58px;
    top: 70px;
    display: flex;
    align-items: center;
    gap: 14px;
  }
  .brand-mark {
    width: 22px;
    height: 22px;
    background: var(--gold);
  }
  .brand-name {
    font-family: "Crimson Pro", serif;
    font-weight: 600;
    color: var(--navy);
    line-height: 1;
  }
  .brand-name .primary {
    display: block;
    font-size: 34px;
    letter-spacing: 0.5px;
  }
  .brand-name .secondary {
    display: block;
    font-size: 17px;
    letter-spacing: 5.5px;
    margin-top: 4px;
  }
  .footer-rule {
    position: absolute;
    left: 59px;
    top: 1034px;
    width: 700px;
    height: 1px;
    background: var(--gold);
    opacity: 0.8;
  }
  .contact {
    position: absolute;
    left: 58px;
    top: 1055px;
    margin: 0;
    padding: 0;
    list-style: none;
    font-family: "Lato", sans-serif;
    font-size: 14px;
    color: var(--text);
  }
  .contact li {
    display: flex;
    align-items: center;
    gap: 8px;
    height: 19px;
  }
  .contact svg { width: 11px; height: 11px; fill: var(--gold); }
  .address {
    position: absolute;
    right: 61px;
    top: 1055px;
    text-align: right;
    font-family: "Lato", sans-serif;
    font-size: 14px;
    line-height: 19px;
    color: var(--text);
    font-style: normal;
  }
  .address .company {
    display: block;
    font-weight: 700;
    color: var(--gold);
  }
  .base-band {
    position: absolute;
    left: 0;
    bottom: 0;
    width: 820px;
    height: 13px;
  }
</style>
</head>
<body>
<div class="canvas">
  <section class="sheet">
    <header class="brand">
      <span class="brand-mark"></span>
      <span class="brand-name">
        <span class="primary">HARBORLINE</span>
        <span class="secondary">STRATEGIES</span>
      </span>
    </header>

    <div class="footer-rule"></div>

    <ul class="contact">
      <li>
        <svg viewBox="0 0 12 12"><path d="M2.5 1l2 2.2-1 1.3c.7 1.5 1.8 2.6 3.2 3.3l1.3-1 2.2 2-1.2 1.6C5 10.2 1.8 7 .9 2.2z"/></svg>
        (555) 014-2290
      </li>
      <li>
        <svg viewBox="0 0 12 12"><path d="M0 2.5h12v7H0z M0 2.5l6 4 6-4" stroke="#fff" stroke-width="0.8"/></svg>
        nora@noravale.com
      </li>
      <li>
        <svg viewBox="0 0 12 12"><circle cx="6" cy="6" r="5.5"/><path d="M6 .5v11M.5 6h11" stroke="#fff" stroke-width="0.8"/></svg>
        noravale.com
      </li>
    </ul>

    <address class="address">
      <span class="company">HARBORLINE STRATEGIES</span>
      218 Alder Street #310<br>
      Fairbanks, AK 99701
    </address>

    <svg class="base-band" viewBox="0 0 820 13" preserveAspectRatio="none">
      <polygon points="0,0 590,0 581,13 0,13" fill="var(--navy)"/>
      <polygon points="596,0 820,0 820,13 587,13" fill="var(--gold-band)"/>
    </svg>
  </section>
</div>
</body>
</html>
```